Velbrin Redesign of Website

I require my webpage to look different but this is out with my current providers platform
I will benefit from designs that use my wording (this is extremely important). I appreciate there may be a lot of wording in some areas so i would be happy with "read more" in various places. The use of my face in photo is a must and my logo is also a must which can be found on m y website www.velbrinadhd.co.uk I do not want corporate feel, i would like a warm, authentic. personal and inviting feel.

```html
<!DOCTYPE html>
<html lang="en">
<head>
<meta charset="utf-8">
<title>Velbrin ADHD Coaching &amp; Wellbeing – The Story</title>
<link href="https://fonts.googleapis.com/css2?family=Cormorant+Garamond:wght@500;600;700&family=Lato:wght@400;700&display=swap" rel="stylesheet">
<style>
:root{
  --teal:#14a58b;
  --gold:#d6b35e;
  --ink:#2f3a36;
  --icon:#34433d;
  --muted:#5d6662;
  --cream:#f7f3ea;
  --mint:#eef7f4;
  --card:#fbfaf7;
  --line:#e6dfcf;
  --forest:#3e4b40;
  --forest-dark:#344036;
  --white:#ffffff;
}
*{box-sizing:border-box;margin:0;padding:0}
html,body{width:1200px;height:4167px;overflow:hidden}
body{position:relative;background:var(--white);font-family:"Lato",sans-serif;color:var(--ink)}
.serif{font-family:"Cormorant Garamond",serif}
section,header,footer{position:absolute;left:0;width:1200px}
.abs{position:absolute}
.btn{position:absolute;display:flex;align-items:center;justify-content:center;color:var(--white);font-weight:700;font-size:13px;letter-spacing:.3px;text-transform:uppercase}
.photo{position:absolute}

/* header */
.site-header{top:0;height:56px;background:var(--white)}
.menu{left:108px;top:19px;display:flex;align-items:center;gap:6px;font-size:15px}
.brand{right:108px;top:14px;display:flex;align-items:center;gap:7px;font-size:14px;font-weight:700;color:var(--teal)}
.brand i{width:14px;height:14px;border-radius:50%;background:var(--teal);display:block}

/* hero */
.hero{top:56px;height:554px;background:linear-gradient(160deg,#8fa99f 0%,#b8cbc4 45%,#d3ded9 100%)}
.hero-foliage{right:0;top:0;width:233px;height:554px;background:linear-gradient(90deg,#8aa597,#5d7c6a)}
.hero h1{left:108px;top:140px;font-size:54px;line-height:60px;font-weight:600;color:#2c3531;letter-spacing:.5px}
.hero h1 span{color:var(--teal)}
.hero p{left:108px;top:287px;width:400px;font-size:19px;line-height:28px;color:#2c3531}
.hero .btn{left:108px;top:368px;width:217px;height:45px;background:var(--teal)}
.hero-frame{left:680px;top:51px;width:437px;height:447px;border:2px solid var(--gold);border-radius:90px 20px 20px 20px}
.hero-portrait{left:661px;top:62px;width:440px;height:440px;border-radius:80px 20px 20px 20px;background:linear-gradient(180deg,#9fb4bd 0%,#c9b7a3 50%,#2f5a5c 100%)}

/* about */
.about{top:610px;height:684px}
.about-photo{left:108px;top:110px;width:433px;height:485px;background:linear-gradient(180deg,#eeeeee,#dcd6cf)}
.about h2{left:582px;top:150px;font-size:38px;line-height:49px;font-weight:600;color:var(--teal);text-transform:uppercase}
.about p{left:585px;top:278px;width:495px;font-size:12.5px;line-height:26.8px;color:var(--ink)}
.about .btn{left:582px;top:519px;width:178px;height:34px;background:var(--gold);font-weight:400}

/* journey */
.journey{top:1294px;height:1002px;background:var(--cream)}
.section-title{left:0;width:1200px;text-align:center;font-size:46px;line-height:56px;font-weight:600;color:var(--teal);text-transform:uppercase;letter-spacing:.5px}
.journey .journey-title{top:90px}
.journey .path-title{top:637px}
.j-card{position:absolute;width:482px;height:117px;border:1.5px solid var(--line);border-radius:8px;background:var(--cream)}
.j-icon{position:absolute;left:18px;top:18px;width:58px;height:58px;border-radius:50%;background:#efe6d1;display:flex;align-items:center;justify-content:center}
.j-text{position:absolute;left:97px;top:14px;right:12px;font-size:12.8px;line-height:18px}
.j-text b{display:block;font-weight:700;color:var(--ink);margin-bottom:8px}
.j-text span{display:block;font-weight:400}
.j-text a{display:block;color:var(--teal);margin-top:8px;text-decoration:none}
.j-note{left:359px;top:470px;width:482px;height:81px}
.j-note .j-icon{top:11px}
.j-note .j-text{top:12px;left:97px;font-size:11px;line-height:16px}
.path{left:108px;top:733px;width:984px;height:160px}
.path-line{position:absolute;left:48px;right:48px;top:49px;border-top:1.5px dashed #c9bfa6}
.step{position:absolute;top:0;width:123px;text-align:center}
.step .num{font-size:26px;color:var(--gold);font-family:"Lato",sans-serif;line-height:26px}
.step .dot{width:32px;height:32px;border-radius:50%;background:var(--icon);margin:9px auto 0;display:flex;align-items:center;justify-content:center;position:relative}
.step .pic{width:98px;height:62px;margin:9px auto 0}
.step .label{font-size:11.5px;font-weight:700;line-height:15px;margin-top:5px}

/* approach */
.approach{top:2296px;height:582px}
.approach h2{left:108px;top:86px;font-size:41px;font-weight:600;color:var(--teal);text-transform:uppercase}
.a-card{position:absolute;top:167px;width:234px;height:327px;background:var(--card);border-radius:6px;overflow:hidden}
.a-card .pic{height:157px;width:100%}
.a-card h3{margin:22px 13px 0;font-size:12.5px;font-weight:700}
.a-card p{margin:10px 13px 0;font-size:11.3px;line-height:20px;color:var(--muted)}
.a-card a{display:block;margin:10px 13px 0;font-size:11px;color:var(--gold);text-decoration:none}

/* testimonials */
.testimonials{top:2878px;height:405px;background:var(--mint)}
.testimonials .section-title{top:72px}
.t-card{position:absolute;top:170px;width:315px;height:137px;background:#f8fbfa;border-radius:4px}
.t-avatar{position:absolute;left:15px;top:12px;width:58px;height:58px;border-radius:50%}
.t-card p{position:absolute;left:93px;top:12px;right:12px;font-size:11.3px;line-height:20.5px;color:var(--muted)}
.t-card b{position:absolute;left:93px;top:105px;font-size:11.5px}
.dots{left:574px;top:348px;display:flex;gap:7px}
.dots i{width:12px;height:12px;border-radius:50%;background:var(--icon);display:block}
.dots i:first-child{background:var(--gold)}

/* cta */
.cta{top:3367px;height:255px}
.cta-box{left:175px;top:0;width:850px;height:255px;background:var(--gold);border-radius:16px;overflow:hidden}
.cta-photo{right:0;top:0;width:340px;height:255px;background:linear-gradient(90deg,var(--gold) 0%,#a9a48f 30%,#5f7a7b 70%,#c6b6a3 100%)}
.cta h2{left:27px;top:30px;width:480px;font-size:33px;line-height:40px;font-weight:500;color:var(--white)}
.cta .btn{left:27px;top:178px;width:212px;height:34px;background:var(--teal);border-radius:6px;font-weight:700}

/* footer */
.site-footer{top:3680px;height:487px}
.footer-wave{left:0;top:0}
.footer-body{left:0;top:40px;width:1200px;height:447px;background:linear-gradient(180deg,var(--forest-dark),var(--forest))}
.f-brand{left:108px;top:175px;width:280px;text-align:center;color:#6fa5a8}
.f-brand .mark{width:70px;height:70px;border-radius:50%;background:#6fa5a8;margin:0 auto 12px}
.f-brand b{display:block;font-size:16px;font-weight:700;color:#7fb3b5}
.f-brand small{display:block;font-size:7px;letter-spacing:2.6px;color:#b6b09e;margin-top:6px;text-transform:uppercase;white-space:nowrap}
.f-col h4{font-size:17px;font-weight:700;color:var(--white);letter-spacing:.2px}
.f-links{left:422px;top:138px}
.f-links ul{list-style:none;margin-top:12px}
.f-links li{font-size:12.5px;color:#e7ebe6;line-height:31px}
.f-contact{left:606px;top:138px}
.c-row{display:flex;align-items:flex-start;gap:12px;margin-top:16px;font-size:12.5px;line-height:17px;color:#e7ebe6}
.c-icon{flex:none;width:27px;height:27px;border-radius:50%;background:var(--gold);display:flex;align-items:center;justify-content:center}
.f-social{left:941px;top:138px}
.f-social .c-icon{margin-top:14px;width:32px;height:32px}
.f-rule{left:108px;top:439px;width:984px;border-top:1px solid #87928a}
.copyright{left:0;top:455px;width:1200px;text-align:center;font-size:11px;color:#dfe4df}
</style>
</head>
<body>

<header class="site-header">
  <div class="abs menu">
    <svg width="24" height="14" viewBox="0 0 24 14"><path d="M0 1h24M0 7h24M0 13h24" stroke="#2f3a36" stroke-width="1.6"/></svg>
    MENU
  </div>
  <div class="abs brand"><i></i>Velbrin</div>
</header>

<section class="hero">
  <div class="abs hero-foliage" role="img" aria-label="Leafy green foliage at the page edge"></div>
  <h1 class="abs serif">THE STORY<br>BEHIND <span>VELBRIN</span></h1>
  <p class="abs">Helping others began with understanding myself.</p>
  <a class="btn">Book a Discovery Call</a>
  <div class="abs hero-frame"></div>
  <div class="photo hero-portrait" role="img" aria-label="Portrait of the founder by a misty lake"></div>
</section>

<section class="about">
  <div class="photo about-photo" role="img" aria-label="Founder seated in a white blouse, smiling"></div>
  <h2 class="abs serif">Hello,<br>I'm Morven Ashby Hale</h2>
  <p class="abs">Founder of Velbrin ADHD Coaching &amp; Wellbeing Lorem ipsum dolor sit amet, consectetur adipiscing elit. Sed non mollis felis. Maecenas vel finibus enim, sit amet vulputate risus. Quisque rutrum ex at erat ullamcorper, nec faucibus eros viverra. Donec neque metus, pharetra vitae ex in, facilisis finibus elit. Vivamus elementum erat eu condimentum tempus. Aliquam eget fringilla ligula. Aliquam quis feugiat sem, a malesuada elit. Pellentesque lacinia enim ante, in egestas lacus maximus a. Praesent sit amet rutrum enim, id blandit dui. Cras ac mattis purus. Vivamus nec neque tincidunt, facilisis ligula in, ultricies felis.</p>
  <a class="btn">Learn More</a>
</section>

<section class="journey">
  <h2 class="abs section-title journey-title serif">My Journey</h2>

  <div class="j-card" style="left:108px;top:190px">
    <div class="j-icon"><svg width="30" height="30" viewBox="0 0 30 30" fill="none" stroke="#34433d" stroke-width="1.8"><circle cx="15" cy="15" r="11"/><path d="M15 4v22M9 10c3 0 6 2 6 5M21 10c-3 0-6 2-6 5M9 20c3 0 6-2 6-5M21 20c-3 0-6-2-6-5"/></svg></div>
    <div class="j-text"><b>My adult ADHD diagnosis came during a period of profound self-discovery following a mental health breakdown</b><span>Lorem ipsum dolor sit amet, consectetur adipiscing elit. Sed</span><a>Read More</a></div>
  </div>
  <div class="j-card" style="left:610px;top:190px">
    <div class="j-icon"><svg width="30" height="30" viewBox="0 0 30 30" fill="none" stroke="#34433d" stroke-width="1.8"><path d="M6 12c0 8 4 13 9 13s9-5 9-13z"/><path d="M10 12V6M15 12V4M20 12V6"/></svg></div>
    <div class="j-text"><b>This personal journey inspire to me deepen my professional knowledge and training.</b><span>Lorem ipsum dolor sit amet, consectetur adipiscing elit. Sed</span><a>Read More</a></div>
  </div>
  <div class="j-card" style="left:108px;top:331px">
    <div class="j-icon"><svg width="30" height="30" viewBox="0 0 30 30" fill="none" stroke="#34433d" stroke-width="1.8"><path d="M15 15c-3-4-5-5-7.5-5a5 5 0 000 10c2.5 0 4.5-1 7.5-5s5-5 7.5-5a5 5 0 010 10c-2.5 0-4.5-1-7.5-5z"/></svg></div>
    <div class="j-text"><b>As my understanding grew , I recognized I am also autistic something that is common along side&nbsp; ADHD</b><span>Lorem ipsum dolor sit amet, consectetur adipiscing elit. Sed</span><a>Read More</a></div>
  </div>
  <div class="j-card" style="left:610px;top:331px">
    <div class="j-icon"><svg width="30" height="30" viewBox="0 0 30 30" fill="none" stroke="#34433d" stroke-width="2"><path d="M3 12l12-6 12 6-12 6z"/><path d="M8 15v6c4 3 10 3 14 0v-6M27 12v7"/></svg></div>
    <div class="j-text"><b>These experience strengthened my passion for helping neoro divergent..</b><span>Lorem ipsum dolor sit amet, consectetur adipiscing elit. Sed .</span><a>Read More</a></div>
  </div>
  <div class="j-card j-note">
    <div class="j-icon"><svg width="30" height="30" viewBox="0 0 30 30" fill="none" stroke="#34433d" stroke-width="1.8"><path d="M5 8h16v10H12l-5 4v-4H5z"/><path d="M13 11c-2-2-4 1-1 3 3-2 1-5-1-3z"/></svg></div>
    <div class="j-text">I believe learning never stop, and i continue to develop my knowledge in neurodiversity, wellbeing and mental health so i can offer the best possible support.</div>
  </div>

  <h2 class="abs section-title path-title serif">My Path</h2>
  <div class="abs path">
    <div class="path-line"></div>
    <div class="step" style="left:0"><div class="num">01</div><div class="dot"><svg width="16" height="16" viewBox="0 0 16 16" fill="none" stroke="#d6b35e" stroke-width="1.4"><path d="M2 8l6-5 6 5M4 7v6h8V7"/></svg></div><div class="pic" style="background:linear-gradient(135deg,#2e4a6b,#c9d2dc)" role="img" aria-label="Officer working at a desk"></div><div class="label">Housing<br>Officer</div></div>
    <div class="step" style="left:123px"><div class="num">02</div><div class="dot"><svg width="16" height="16" viewBox="0 0 16 16" fill="none" stroke="#d6b35e" stroke-width="1.4"><circle cx="8" cy="8" r="6"/><path d="M8 2v12"/></svg></div><div class="pic" style="background:linear-gradient(135deg,#e4e0da,#8a8580)" role="img" aria-label="Person resting head in hands"></div><div class="label">Mental Health<br>Breakdown</div></div>
    <div class="step" style="left:246px"><div class="num">03</div><div class="dot"><svg width="16" height="16" viewBox="0 0 16 16" fill="none" stroke="#d6b35e" stroke-width="1.4"><circle cx="8" cy="6" r="4"/><path d="M8 10v4"/></svg></div><div class="pic" style="background:linear-gradient(135deg,#d8d5cf,#7c8a8e)" role="img" aria-label="Tablet and notes on a desk"></div><div class="label">ADHD<br>Diagnosis</div></div>
    <div class="step" style="left:369px"><div class="num">04</div><div class="dot"><svg width="16" height="16" viewBox="0 0 16 16" fill="none" stroke="#d6b35e" stroke-width="1.4"><path d="M8 8c-2-3-3-3-4.5-3a3 3 0 000 6C5 11 6 11 8 8s3-3 4.5-3a3 3 0 010 6C11 11 10 11 8 8z"/></svg></div><div class="pic" style="background:linear-gradient(135deg,#3f8a4a,#d2c04e 50%,#3b6fb0)" role="img" aria-label="Colourful puzzle pieces in hands"></div><div class="label">Understanding<br>Autism</div></div>
    <div class="step" style="left:492px"><div class="num">05</div><div class="dot"><svg width="16" height="16" viewBox="0 0 16 16" fill="none" stroke="#d6b35e" stroke-width="1.4"><path d="M2 3h5v10H2zM9 3h5v10H9z"/></svg></div><div class="pic" style="background:linear-gradient(135deg,#cfd6da,#5a6a78)" role="img" aria-label="Counselling session between two people"></div><div class="label">Integrative<br>Counselling</div></div>
    <div class="step" style="left:615px"><div class="num">06</div><div class="dot"><svg width="16" height="16" viewBox="0 0 16 16" fill="none" stroke="#d6b35e" stroke-width="1.4"><path d="M1 6l7-3 7 3-7 3z"/><path d="M4 8v3c2 2 6 2 8 0V8"/></svg></div><div class="pic" style="background:linear-gradient(135deg,#8a5a4a,#d6cbbf)" role="img" aria-label="Group around a table in a workshop"></div><div class="label">Health &amp; Wellbeing<br>Coach</div></div>
    <div class="step" style="left:738px"><div class="num">07</div><div class="dot"><svg width="16" height="16" viewBox="0 0 16 16" fill="none" stroke="#d6b35e" stroke-width="1.4"><path d="M3 11V8a5 5 0 0110 0v3M3 11h2v3H3zM11 11h2v3h-2z"/></svg></div><div class="pic" style="background:linear-gradient(135deg,#dfe6e8,#6e8a96)" role="img" aria-label="Training session in a bright room"></div><div class="label">Specialist Training<br>in Autism ADHD</div></div>
    <div class="step" style="left:861px"><div class="num">08</div><div class="dot"><svg width="16" height="16" viewBox="0 0 16 16" fill="none" stroke="#d6b35e" stroke-width="1.4"><path d="M8 3l6 10H2z"/><path d="M5 10h6"/></svg></div><div class="pic" style="background:linear-gradient(135deg,#b9c3cb,#4a4f55)" role="img" aria-label="Stacked balancing stones"></div><div class="label">Velbrin<br>Created</div></div>
  </div>
</section>

<section class="approach">
  <h2 class="abs serif">The Velbrin Approach</h2>
  <div class="a-card" style="left:108px"><div class="pic" style="background:linear-gradient(160deg,#e6c87a,#6b6a3a 60%,#3a4a2c)" role="img" aria-label="Person walking along a leafy path"></div><h3>Lived &amp; Tested</h3><p>Lorem ipsum dolor sit amet, consectetur adipiscing elit. Sed non mollis felis. Maecenas vel finibus enim, sit amet vulputate risus.</p><a>Learn More ›</a></div>
  <div class="a-card" style="left:358px"><div class="pic" style="background:linear-gradient(160deg,#e7d7c2,#8a6a50 55%,#3a4550)" role="img" aria-label="Friends laughing together outdoors"></div><h3>Individual, Not one size fits all</h3><p>Lorem ipsum dolor sit amet, consectetur adipiscing elit. Sed non mollis felis. Maecenas vel finibus enim, sit amet vulputate risus.</p><a>Learn More ›</a></div>
  <div class="a-card" style="left:608px"><div class="pic" style="background:linear-gradient(180deg,#dfe4e6,#b5a08a 60%,#6e6660)" role="img" aria-label="Balanced stones on a beach"></div><h3>Practical and sustainable</h3><p>Lorem ipsum dolor sit amet, consectetur adipiscing elit. Sed non mollis felis. Maecenas vel finibus enim, sit amet vulputate risus.</p><a>Learn More ›</a></div>
  <div class="a-card" style="left:858px"><div class="pic" style="background:linear-gradient(160deg,#5c8a5a,#c9c3b8 55%,#8a8f94)" role="img" aria-label="Two people holding hands in support"></div><h3>Compassionate and neuron affirming</h3><p>Lorem ipsum dolor sit amet, consectetur adipiscing elit. Sed non mollis felis. Maecenas vel finibus enim, sit amet vulputate risus.</p><a>Learn More ›</a></div>
</section>

<section class="testimonials">
  <h2 class="abs section-title serif">What Clients Are Saying</h2>
  <div class="t-card" style="left:108px"><div class="t-avatar" style="background:#c9c2bb" role="img" aria-label="Client photo"></div><p>Lorem ipsum dolor sit amet, consectetur adipiscing elit. Sed non mollis felis. Maecenas vel finibus enim, sit amet vulputate risus.</p><b>Hannah R</b></div>
  <div class="t-card" style="left:442px"><div class="t-avatar" style="background:#5a5450" role="img" aria-label="Client photo"></div><p>Lorem ipsum dolor sit amet, consectetur adipiscing elit. Sed non mollis felis. Maecenas vel finibus enim, sit amet vulputate risus.</p><b>Owen Carlisle</b></div>
  <div class="t-card" style="left:777px"><div class="t-avatar" style="background:linear-gradient(135deg,#e2a98a,#3b86c4)" role="img" aria-label="Client photo"></div><p>Lorem ipsum dolor sit amet, consectetur adipiscing elit. Sed non mollis felis. Maecenas vel finibus enim, sit amet vulputate risus.</p><b>Tess Morrow</b></div>
  <div class="abs dots"><i></i><i></i><i></i></div>
</section>

<section class="cta">
  <div class="abs cta-box">
    <div class="photo cta-photo" role="img" aria-label="Group of hands stacked together"></div>
    <h2 class="abs serif">You don't need to do this alone. Together we'll build strategies that actually work.</h2>
    <a class="btn">Book Discovery Call</a>
  </div>
</section>

<footer class="site-footer">
  <svg class="abs footer-wave" width="1200" height="42" viewBox="0 0 1200 42" preserveAspectRatio="none"><path d="M0 20C180 4 330 30 520 22S860 2 1010 14 1150 32 1200 26V42H0z" fill="#344036"/></svg>
  <div class="abs footer-body">
    <div class="abs f-brand"><div class="mark"></div><b>Velbrin</b><small>Empower your mind, transform your life</small></div>
    <div class="abs f-col f-links"><h4>QUICK LINKS</h4><ul><li>Home</li><li>About</li><li>ADHD</li><li>Coaching</li><li>Resources</li><li>Blog</li><li>Contact</li></ul></div>
    <div class="abs f-col f-contact"><h4>CONTACT US</h4>
      <div class="c-row"><span class="c-icon"><svg width="13" height="13" viewBox="0 0 14 14" fill="none" stroke="#fff" stroke-width="1.4"><path d="M7 13s4.5-4.5 4.5-7.5a4.5 4.5 0 00-9 0C2.5 8.5 7 13 7 13z"/><circle cx="7" cy="5.5" r="1.5"/></svg></span><span>Tarrow House Mill Lane Brackley<br>Northshire NB4 2QT</span></div>
      <div class="c-row"><span class="c-icon"><svg width="13" height="13" viewBox="0 0 14 14" fill="none" stroke="#fff" stroke-width="1.4"><rect x="1.5" y="3" width="11" height="8" rx="1"/><path d="M1.5 3.5L7 8l5.5-4.5"/></svg></span><span style="margin-top:5px">Morven@Velbrinadhd.Co.Uk</span></div>
      <div class="c-row"><span class="c-icon"><svg width="13" height="13" viewBox="0 0 14 14" fill="none" stroke="#fff" stroke-width="1.4"><path d="M3 1.5l2 .5 1 3-1.5 1a7 7 0 003.5 3.5l1-1.5 3 1 .5 2c-1 1.5-3 1.5-5 .5A10 10 0 011.5 5C.5 3 1.5 2 3 1.5z"/></svg></span><span style="margin-top:5px">0300 555 0192</span></div>
    </div>
    <div class="abs f-col f-social"><h4>SOCIAL MEDIA</h4>
      <div class="c-icon"></div><div class="c-icon"></div><div class="c-icon"></div>
    </div>
    <div class="abs f-rule"></div>
    <div class="abs copyright">© 2026. ALL RIGHTS RESERVED.</div>
  </div>
</footer>

</body>
</html>
```